"The Summit Hour Audio Series" needs 3 banner ad designs

I am seeking the design and creation of 3 differently-designed ”banner ads.” I want them to look as though there is a relation between designs but I don't want them to look the same.
While compatibility is desired, that desire should not be interpreted as sameness.

I need a series of banner ads to be a supplement and a complement to
"The Summit Hour"'s main banner ad page and accompanying site.
http://www.quorvale.org/

I am looking for high quality, creative capturing of banner ads that focus on three topic areas, namely, my:

1. Leadership Coaching Program –
“Stride Builder Mentoring Track™”

2. Training program – “The Craft of a Steady Captain”

and

3. Speaker Interest & Availability banner ad.

It is desired that each banner, and the banners collectively, complement and fit in with the look and feel of the existing, principal banner and the show’s vision and mission. (in the attachment, I have included a copy of this banner for your information).

The final design should commit experience, competence, depth and reliability.

To provide a bit of context for this request, I have included the show's vision and mission statement as well as a brief description of my perspective on each banner ad.

I will of course, provide the winner all of the information, documents, graphic depictions, etc that I have available (during the handover stage) that will enable them to create quality products.

In addition, each banner ad should be delivered as JPEG files in dimensions 728 pixel wide and 90 pixels high each. The following fonts: Trajan Pro Regular or Thomas Condensed Regular are the desired fonts.

The task summary: Design 3 banner ads as described below:

1. Leadership Coaching Program – Stride Builder Mentoring Track™
My coaching program has a formal structure that has an existing graphic capturing of leadership coaching that that would/should be incorporated in the ad.

2. Training program – The Craft of a Steady Captain
The skills training program description I have included as noted below; it is a program that can also be licensed for use by customers who would wish to use it in their organization. In addition to the creative thinking of graphics artists, it would probably be useful to view the home page graphic at www.tovrik4.com. This image might be useful in enhancing the banner ad graphic.

3. Speaking Interest – Availability
Have been and desire using this banner to communicate my interest in generating value and availability as a speaker.

-Vision-
“The Summit Hour”
Making an Impact through Effective Leadership
*is a powerfully engaging platform for great conversations about leadership and leadership learning.

-Mission-
Build a community of listeners who are informed and enthusiastically engaged with the host and the show’s goal of improving the quality of leadership wherever listeners are living and leading.

File: "1785 Postcard V2" - *this information is for use in designing the
Leadership Coaching Banner Ad* = *Stride Builder Mentoring Track*

File: "Cover Shot of Skills Book" - *this information is
for use in designing the Book Ad – The Craft of a Steady Captain:
Growing a Guide Whom Peers Gladly Trust*

File: (word doc) The Craft of a Steady Captain Training Workshop – Skills &
Concepts Summary *this information is for the design of the banner ad for
the Skills Training Course. It includes quotes that could be excerpted to
include in the banner ad*

File name: "Cover - Craft of a Steady Captain"
-> Picture of book for Craft of a Steady Captain Training Program – *this is additional information for the use in designing the Training program banner ad

You can find the other attachments useful. Please have a look.
I welcome all your creative and original designs. Remember, these are 3 different-looking banner ads - though related in some way.

Project Deadline Extended Reason: The current designs have not included enough variety and creativity. While I am desirous of compatibility of the ad renditions with the central image, I am not interpreting compatibility with sameness of looking to see the same image in each banner ad. I rather think the image differentiation promotes both interest and distinction between the products of book, leadership coaching, speaking, etc. Same image embedded in each banner ad doesn't provide the variety that I think both distinguishes and draws interest. In this regard, most of the current examples include the same pictorial images across designs and the use of just words vs. images from among those provided, As an example a picture of my book on the book banner ad seems more impactful than merely using the words book on the ad for the book; and the picture of a speaker vs. Speaker Availability.I hope this feedback is helpful . Regards,Leopold Added Saturday, June 3, 2017

Target Market(s)

Online Radio Listeners Can Visit WavelineHub.com for examples - Will be broadcast on the Commerce Channel

Industry/Entity Type

Business Consultant

Colors

Designer to choose colors to be used in the design.

Requirements
Should not have
• Anything that doesn't speak to the characteristics noted at the end of the summary provided in the description above

```html
<!DOCTYPE html>
<html lang="en">
<head>
<meta charset="utf-8">
<title>Speaking Interest – Availability Banner</title>
<link rel="stylesheet" href="https://fonts.googleapis.com/css2?family=Cinzel:wght@400;500&display=swap">
<style>
  :root {
    --navy: #0a2a80;
    --royal: #1c4aa6;
    --sky: #6f95d2;
    --mist: #dfe7f3;
    --white: #ffffff;
    --mic-dark: #0c2770;
    --mic-light: #3c5fa8;
    --suit-dark: #3a3a40;
    --suit-light: #f4f4f6;
  }
  html, body {
    margin: 0;
    padding: 0;
    width: 1200px;
    height: 148px;
    overflow: hidden;
    background: var(--white);
  }
  .banner {
    position: relative;
    width: 1200px;
    height: 148px;
    overflow: hidden;
    background: linear-gradient(90deg,
      var(--navy) 0%,
      var(--navy) 18%,
      var(--royal) 40%,
      var(--sky) 58%,
      var(--mist) 70%,
      var(--white) 80%,
      var(--white) 100%);
  }
  .banner__mic {
    position: absolute;
    left: 0;
    top: 0;
    width: 165px;
    height: 148px;
    background: radial-gradient(ellipse at 40% 30%, var(--mic-light) 0%, var(--mic-dark) 70%);
  }
  .banner__title {
    position: absolute;
    left: 300px;
    top: 16px;
    width: 390px;
    text-align: center;
    color: var(--white);
    font-family: "Cinzel", "Trajan Pro", Georgia, serif;
  }
  .banner__kicker {
    margin: 0;
    font-size: 26px;
    font-weight: 400;
    letter-spacing: 1px;
    line-height: 36px;
    font-variant: small-caps;
    text-transform: lowercase;
  }
  .banner__kicker::first-letter { text-transform: uppercase; }
  .banner__kicker .cap { text-transform: uppercase; }
  .banner__rule {
    display: block;
    width: 372px;
    height: 2px;
    margin: 10px auto 6px;
    background: var(--white);
  }
  .banner__headline {
    margin: 0;
    font-size: 52px;
    font-weight: 400;
    line-height: 54px;
    letter-spacing: 1px;
    font-variant: small-caps;
  }
  .banner__speaker {
    position: absolute;
    right: 0;
    top: 0;
    width: 215px;
    height: 148px;
    background: linear-gradient(180deg, var(--suit-light) 0%, var(--suit-light) 8%, var(--suit-dark) 45%, var(--suit-dark) 100%);
    clip-path: polygon(30% 100%, 30% 55%, 40% 38%, 47% 5%, 62% 0%, 72% 8%, 74% 38%, 88% 48%, 95% 100%);
  }
</style>
</head>
<body>
  <div class="banner">
    <div class="banner__mic" role="img" aria-label="Photo of a stage microphone on a stand against deep blue"></div>
    <div class="banner__title">
      <p class="banner__kicker"><span class="cap">S</span>peaking <span class="cap">I</span>nterest</p>
      <span class="banner__rule"></span>
      <p class="banner__headline"><span>A</span>vailability</p>
    </div>
    <div class="banner__speaker" role="img" aria-label="Photo of the host standing in a dark suit and tie"></div>
  </div>
</body>
</html>
```